Visual consulting framework

Tamsworth Advisory is a financial consulting business that takes it clients on the following journey:
1. Get fit (disciplined)
2. Get funded (access to capital)
3. Get big (grow)
4. Get out (exit with wealth)
Over thirty years we have identified that the key to being successful on this journey are the following elements or components.
1. Vision
2. Strategy
3. Structure
4. Product & services
5. Sales and marketing
6. System and processes
7. People
8. Culture
9. Finance
10. M&A
11. Performance monitoring
12. Risk management
We require a visual representation of these elements and the journey to communicate to clients and prospects in marketing material.

```html
<!DOCTYPE html>
<html lang="en">
<head>
<meta charset="utf-8">
<title>Tamsworth Advisory – Consulting Framework</title>
<link rel="stylesheet" href="https://fonts.googleapis.com/css2?family=Baloo+2:wght@500;700&display=swap">
<style>
  :root {
    --orange: #F7931E;
    --blue: #0AA5E8;
    --page: #E5E5E5;
    --card: #FFFFFF;
    --band: #F1F1F1;
    --white: #FFFFFF;
  }
  * { margin: 0; padding: 0; box-sizing: border-box; }
  html, body { width: 1200px; height: 720px; overflow: hidden; background: var(--page); }
  body { position: relative; font-family: "Baloo 2", sans-serif; }
  .card { position: absolute; left: 65px; top: 59px; width: 1070px; height: 602px; background: var(--card); }
  .band { position: absolute; height: 28px; background: linear-gradient(90deg, var(--band), var(--band) 85%, rgba(241,241,241,0)); }
  .band--top { left: 287px; top: 109px; width: 793px; }
  .band--bottom { left: 271px; top: 402px; width: 809px; }
  .journey { position: absolute; left: 0; top: 0; width: 1200px; height: 720px; }
  .pill {
    position: absolute; width: 167px; height: 75px; border-radius: 38px;
    display: flex; align-items: center; justify-content: center; text-align: center;
    font-weight: 700; font-size: 17px; line-height: 20px;
  }
  .pill--element { background: var(--orange); color: var(--white); }
  .pill--outline { background: var(--white); color: var(--blue); border: 1.5px solid var(--blue); }
  .stage {
    position: absolute; width: 130px; text-align: center; color: var(--blue);
    font-weight: 700; font-size: 17px; line-height: 20px; transform: translate(-50%, -50%);
  }
  .brand { position: absolute; left: 131px; top: 556px; display: flex; align-items: center; gap: 10px; }
  .brand__mark { width: 40px; height: 40px; border-radius: 50%; background: var(--orange); }
  .brand__name { color: var(--blue); font-weight: 500; font-size: 20px; line-height: 20px; letter-spacing: 1px; text-transform: uppercase; }
</style>
</head>
<body>
  <div class="card"></div>
  <div class="band band--top"></div>
  <div class="band band--bottom"></div>

  <svg class="journey" viewBox="0 0 1200 720" aria-hidden="true">
    <defs>
      <g id="stage-track" fill="none" stroke="var(--blue)" stroke-width="2">
        <path d="M342 183 H442 A37 37 0 0 1 442 257 H358"/>
        <path d="M358 281 H442 A36.5 36.5 0 0 1 442 354 H342"/>
        <polygon points="479,213 487,220 479,227" fill="var(--blue)" stroke="none"/>
        <polygon points="479,311 487,318 479,325" fill="var(--blue)" stroke="none"/>
        <line x1="395" y1="259" x2="395" y2="280" stroke-width="1.2" stroke-dasharray="2 3"/>
        <circle cx="335" cy="271" r="23" fill="var(--white)" stroke-width="1.5"/>
        <circle cx="402" cy="159" r="17" fill="var(--blue)" stroke="none"/>
        <circle cx="402" cy="159" r="7" stroke="var(--white)" stroke-width="2"/>
        <circle cx="402" cy="378" r="17" fill="var(--blue)" stroke="none"/>
        <circle cx="402" cy="378" r="7" stroke="var(--white)" stroke-width="2"/>
      </g>
    </defs>
  </svg>

  <div class="pill pill--element" style="left:121px;top:85px">Perfomance<br>Management</div>
  <div class="pill pill--element" style="left:319px;top:85px">Vision</div>
  <div class="pill pill--element" style="left:497px;top:85px">Strategy</div>
  <div class="pill pill--element" style="left:675px;top:85px">Structure</div>
  <div class="pill pill--element" style="left:854px;top:85px">Product<br>Services</div>

  <div class="pill pill--outline" style="left:121px;top:235px">Risk<br>Management</div>

  <div class="pill pill--element" style="left:319px;top:378px">Systems &amp;<br>Processes</div>
  <div class="pill pill--element" style="left:497px;top:378px">Finance</div>
  <div class="pill pill--element" style="left:675px;top:378px">Sales &amp;<br>Marketing</div>
  <div class="pill pill--element" style="left:854px;top:378px">M &amp; A</div>
  <div class="pill pill--element" style="left:854px;top:469px">People</div>
  <div class="pill pill--element" style="left:854px;top:562px">Culture</div>

  <svg class="journey" viewBox="0 0 1200 720" aria-hidden="true">
    <use href="#stage-track"/>
    <use href="#stage-track" transform="translate(178 0)"/>
    <use href="#stage-track" transform="translate(356 0)"/>
    <use href="#stage-track" transform="translate(535 0)"/>
  </svg>

  <div class="stage" style="left:407px;top:221px">Get Fit</div>
  <div class="stage" style="left:407px;top:318px">Discipline</div>
  <div class="stage" style="left:590px;top:221px">Get Funded</div>
  <div class="stage" style="left:591px;top:321px">Access to<br>Capital</div>
  <div class="stage" style="left:774px;top:221px">Get Big</div>
  <div class="stage" style="left:774px;top:319px">Grow</div>
  <div class="stage" style="left:958px;top:221px">Get out</div>
  <div class="stage" style="left:958px;top:318px">Exit with<br>Wealth</div>

  <div class="brand">
    <div class="brand__mark"></div>
    <div class="brand__name">Tamsworth<br>Advisory</div>
  </div>
</body>
</html>
```